Notary Signing Agent Need Business card Design

Need a Business card design for my new company. RT Belvoni-Strand LLC
Mobile Notary Signing Agent. I go to the customer for closing of Mortgage's Documents . possible signs of honesty, integrity and confidentiality.

Work with Title company to Notary Mortgage closing.

My Target Market is Title companies. Banks and Financial Institution.

Color Blue to Black Professional ) if needed some Green Little Red

And possible a company logo.

Mobile ( travel to clients ) Integrity, Honest Trustworthy. A show of Professional services.

Would like company name and my name on card

Use both sides and front with business name and my name. phone numbers.

Target Market(s)

Title company, Banks mortgage company

Industry/Entity Type

Travel

Contact Information for Business Card

Notary, Certified signing agent, Mobile

Colors
0455a3

Requirements
Must have
• Name of company , owners name phone number,
Nice to have
• blue and black color like a professional look but not limit to these only.
• a stand out from other cards .

```html
<!DOCTYPE html>
<html lang="en">
<head>
<meta charset="utf-8">
<title>RT Belvoni-Strand LLC – Business Card</title>
<link rel="stylesheet" href="https://fonts.googleapis.com/css2?family=Roboto+Condensed:wght@300;700&display=swap">
<style>
  :root {
    --page-bg: #ececec;
    --card-white: #ffffff;
    --brand-indigo: #3a3288;
    --stripe-tint: rgba(255, 255, 255, 0.28);
    --text-light: #ffffff;
  }
  * { margin: 0; padding: 0; box-sizing: border-box; }
  html, body {
    width: 841px;
    height: 1200px;
    overflow: hidden;
    background: var(--page-bg);
  }
  .canvas {
    position: relative;
    width: 841px;
    height: 1200px;
  }
  .card {
    position: absolute;
    left: 114px;
    top: 50px;
    width: 612px;
    height: 1100px;
    background: var(--brand-indigo);
    overflow: hidden;
    font-family: "Roboto Condensed", sans-serif;
    color: var(--text-light);
  }
  .card-backdrop {
    position: absolute;
    inset: 0;
  }
  .company-name {
    position: absolute;
    left: 0;
    width: 100%;
    top: 300px;
    text-align: center;
    font-weight: 700;
    font-size: 46px;
    letter-spacing: 0.3px;
    color: var(--brand-indigo);
  }
  .agent-name {
    position: absolute;
    left: 0;
    width: 100%;
    top: 612px;
    text-align: center;
    font-weight: 700;
    font-size: 43px;
  }
  .agent-role {
    position: absolute;
    left: 0;
    width: 100%;
    top: 684px;
    text-align: center;
    font-weight: 300;
    font-size: 37px;
  }
  .contact-list {
    position: absolute;
    left: 120px;
    top: 792px;
    list-style: none;
  }
  .contact-item {
    display: flex;
    align-items: center;
    height: 56px;
    margin-bottom: 20px;
    font-weight: 300;
    font-size: 46px;
  }
  .contact-icon {
    width: 36px;
    height: 40px;
    margin-right: 12px;
    flex: none;
  }
</style>
</head>
<body>
<div class="canvas">
  <div class="card">
    <svg class="card-backdrop" width="612" height="1100" viewBox="0 0 612 1100" aria-hidden="true">
      <polygon points="0,0 612,0 612,306 306,569 0,306" fill="var(--card-white)"/>
      <polygon points="0,819 0,904 216,1100 278,1100" fill="var(--stripe-tint)"/>
      <polygon points="612,819 612,904 396,1100 334,1100" fill="var(--stripe-tint)"/>
    </svg>

    <div class="company-name">RT Belvoni-Strand LLC</div>

    <div class="agent-name">Daniel R Halvorsen</div>
    <div class="agent-role">Mobile Notary Signing Agent</div>

    <ul class="contact-list">
      <li class="contact-item">
        <svg class="contact-icon" viewBox="0 0 36 40" aria-label="Mobile phone">
          <rect x="8" y="3" width="20" height="34" rx="3" fill="none" stroke="#fff" stroke-width="2.5"/>
          <line x1="8" y1="30" x2="28" y2="30" stroke="#fff" stroke-width="2"/>
          <line x1="15" y1="33.5" x2="21" y2="33.5" stroke="#fff" stroke-width="2"/>
        </svg>
        <span>555-864-2193</span>
      </li>
      <li class="contact-item">
        <svg class="contact-icon" viewBox="0 0 36 40" aria-label="Fax">
          <rect x="10" y="4" width="16" height="14" fill="none" stroke="#fff" stroke-width="2"/>
          <line x1="13" y1="9" x2="23" y2="9" stroke="#fff" stroke-width="1.5"/>
          <line x1="13" y1="13" x2="23" y2="13" stroke="#fff" stroke-width="1.5"/>
          <rect x="3" y="18" width="30" height="18" rx="2" fill="#fff"/>
          <path d="M9 22 h18 v4 h-4 l-2 4 h-6 l-2 -4 h-4 z" fill="var(--brand-indigo)"/>
        </svg>
        <span>555-472-0358</span>
      </li>
    </ul>
  </div>
</div>
</body>
</html>
```